"We are still here" postcard

An employee has left the company and is soliciting clients leaving them to believe I have shut down. Need to convey graphic message that we are still operating and continue the great service they have always had. We prepare income taxes. The office has a train theme within and is located on historic Corwin Street. Some ideas might be yin/yang light/dark up/down steam engine/caboose

Our colors are
98a9b7
3aa9ae
3c4c80
ab3c51

```html
<!DOCTYPE html>
<html lang="en">
<head>
<meta charset="UTF-8">
<title>We Are Still Here – Postcard</title>
<link href="https://fonts.googleapis.com/css2?family=Anton&family=Montserrat:wght@400;500;700&family=Oswald:wght@600&display=swap" rel="stylesheet">
<style>
  :root {
    --backdrop: #e4d2cd;
    --paper: #ffffff;
    --teal: #34a3a8;
    --ink: #2c2f36;
    --rule: #3a3a3a;
    --photo-dark: #1a2433;
    --photo-mid: #2f3e55;
    --white: #ffffff;
  }
  * { box-sizing: border-box; margin: 0; padding: 0; }
  html, body { width: 1200px; height: 1198px; overflow: hidden; }
  body { background: var(--backdrop); position: relative; font-family: "Montserrat", sans-serif; }

  .card { position: absolute; left: 292px; width: 704px; height: 468px; background: var(--paper); overflow: hidden; }
  .card--front { top: 100px; }
  .card--back { top: 614px; }

  .brand { position: absolute; left: 38px; top: 16px; font-family: "Oswald", sans-serif; font-weight: 600; font-size: 24px; color: var(--teal); letter-spacing: 0.5px; }
  .band { position: absolute; left: 0; width: 100%; height: 8px; background: var(--teal); }

  .photo { position: absolute; background: linear-gradient(120deg, var(--photo-dark) 0%, var(--photo-mid) 55%, #24303f 100%); }
  .card--front .photo { left: 0; top: 62px; width: 704px; height: 346px; }
  .card--back .photo { left: 0; top: 0; width: 344px; height: 468px; }

  .headline { position: absolute; font-family: "Anton", sans-serif; color: var(--white); line-height: 1; text-transform: uppercase; }
  .headline span { display: block; }
  .headline .accent { color: var(--teal); }
  .card--front .headline { left: 38px; top: 86px; font-size: 86px; }
  .card--front .headline span + span { margin-top: -2px; }
  .card--back .headline { left: 52px; top: 30px; font-size: 72px; }

  .underline { position: absolute; height: 2px; background: var(--white); }
  .underline::before, .underline::after { content: ""; position: absolute; top: -1px; width: 48px; height: 4px; background: var(--white); }
  .underline::before { left: 0; } .underline::after { right: 0; }
  .card--front .underline { left: 44px; top: 289px; width: 296px; }
  .card--back .underline { left: 52px; top: 182px; width: 244px; }
  .card--back .underline::before, .card--back .underline::after { display: none; }

  .contact { position: absolute; display: flex; align-items: center; gap: 10px; font-size: 13px; }
  .contact svg { width: 18px; height: 18px; }
  .card--front .contact { top: 437px; color: var(--teal); }
  .card--front .contact--mail { left: 52px; }
  .card--front .contact--web { left: 478px; }
  .card--back .contact { top: 436px; color: var(--white); font-size: 11px; gap: 8px; }
  .card--back .contact svg { width: 13px; height: 13px; }
  .card--back .contact--mail { left: 14px; }
  .card--back .contact--web { left: 180px; }

  .divider { position: absolute; left: 344px; top: 0; width: 12px; height: 468px; background: var(--teal); }
  .stamp-box { position: absolute; left: 570px; top: 38px; width: 94px; height: 94px; border: 1.5px solid var(--ink); }
  .address-lines { position: absolute; left: 384px; top: 176px; width: 282px; }
  .address-lines i { display: block; height: 1.5px; background: var(--rule); margin-bottom: 34.5px; }

  .callout { position: absolute; left: 444px; top: 396px; display: flex; align-items: center; gap: 10px; }
  .callout svg { width: 38px; height: 38px; }
  .callout__label { font-size: 14px; color: var(--teal); font-weight: 500; }
  .callout__phone { font-family: "Oswald", sans-serif; font-weight: 600; font-size: 23px; color: var(--ink); line-height: 1.1; }
</style>
</head>
<body>

<section class="card card--front">
  <div class="brand">YOURLOGO</div>
  <div class="band" style="top:54px"></div>
  <div class="photo" role="img" aria-label="Steam locomotive with red buffer beam on a track at dusk, trees behind"></div>
  <div class="band" style="top:408px"></div>
  <h1 class="headline"><span>We Are</span><span><span class="accent" style="display:inline">Still</span> Here</span></h1>
  <div class="underline"></div>
  <div class="contact contact--mail">
    <svg viewBox="0 0 20 20" fill="none" stroke="currentColor" stroke-width="1.6"><rect x="2" y="4" width="16" height="12"/><path d="M2 4l8 7 8-7"/></svg>
    info@corwinledger.com
  </div>
  <div class="contact contact--web">
    <svg viewBox="0 0 20 20" fill="none" stroke="currentColor" stroke-width="1.6"><circle cx="10" cy="10" r="8"/><path d="M2 10h16M10 2c3 3 3 13 0 16M10 2c-3 3-3 13 0 16"/></svg>
    www.corwinledger.com
  </div>
</section>

<section class="card card--back">
  <div class="photo" role="img" aria-label="Front view of a steam locomotive with glowing headlamp and red buffer beam at dusk"></div>
  <h2 class="headline"><span>We Are</span><span><span class="accent" style="display:inline">Still</span> Here</span></h2>
  <div class="underline"></div>
  <div class="contact contact--mail">
    <svg viewBox="0 0 20 20" fill="none" stroke="currentColor" stroke-width="1.8"><rect x="2" y="4" width="16" height="12"/><path d="M2 4l8 7 8-7"/></svg>
    info@youremail.com
  </div>
  <div class="contact contact--web">
    <svg viewBox="0 0 20 20" fill="none" stroke="currentColor" stroke-width="1.8"><circle cx="10" cy="10" r="8"/><path d="M2 10h16M10 2c3 3 3 13 0 16M10 2c-3 3-3 13 0 16"/></svg>
    www.yourwebsite.com
  </div>
  <div class="divider"></div>
  <div class="stamp-box"></div>
  <div class="address-lines"><i></i><i></i><i></i><i></i><i></i><i></i></div>
  <div class="callout">
    <svg viewBox="0 0 40 40" fill="none" stroke="var(--teal)" stroke-width="2.4"><path d="M4 6h20v13H13l-6 5v-5H4z"/><path d="M27 13h9v13h-3v5l-6-5h-9v-4"/><circle cx="10" cy="12.5" r="0.8" fill="var(--teal)"/><circle cx="14" cy="12.5" r="0.8" fill="var(--teal)"/><circle cx="18" cy="12.5" r="0.8" fill="var(--teal)"/></svg>
    <div>
      <div class="callout__label">Call us to find more</div>
      <div class="callout__phone">000 1234 5678</div>
    </div>
  </div>
</section>

</body>
</html>
```